India Export Business Card Design

We are a small company importing from India,
Antique furniture and textiles.
We would like a design with somthing of India in it.
IE: Camels, Tuk Tuks, People or maybe Taj Mahal.
Only one of the above suggestions, we do not want the card to be to busy.
We travel to India twice a year to get the product and then come home to New Zealand and sell it.
And must have our business name which is
Kestrel Trading Company
Nz phone no. 64 9 375 8162
Mobile 64 21 603 174
Email briony@kestreltrading.co.nz
Www.kestreltrading.co.nz

Also my name and position
Briony Calder
Director

Reason: I am awaiting for a design to come back with different colours. Many thanks

Target Market(s)

Indian heritage furniture and textiles in India also
New Zealand market for public to buy the goods that is bought in India

Industry/Entity Type

Travel

Contact Information for Business Card

Kestrel Trading Company
17b Orland Road
RD 5 Papakura 2417
Auckland
New Zealand
email address which will be associated to our new website
website once we have it assigned

Requirements
Must have
• Company name and region.
Phone numbers
My name and title.
Nice to have
• I would like the card to portray India and as i said before, I like the idea of camels in a line with ropes between them like an animation.
But happy to see what other suggestions there are.

```html
<!DOCTYPE html>
<html lang="en">
<head>
<meta charset="utf-8">
<title>Briony Calder – Kestrel Trading Company</title>
<link rel="stylesheet" href="https://fonts.googleapis.com/css2?family=UnifrakturMaguntia&family=Lora:ital@1&display=swap">
<style>
  :root {
    --paper: #ffffff;
    --trim-red: #d52b2b;
    --bleed-blue: #1fb0e6;
    --gold-light: #fbe29c;
    --gold-mid: #f1c26c;
    --gold-deep: #d99a45;
    --ink: #111111;
  }
  html, body {
    margin: 0;
    padding: 0;
    width: 1200px;
    height: 734px;
    overflow: hidden;
    background: var(--paper);
  }
  .canvas {
    position: relative;
    width: 1200px;
    height: 734px;
    background: var(--paper);
  }
  .guide-frame {
    position: absolute;
    inset: 0;
  }
  .card-face {
    position: absolute;
    left: 39px;
    top: 44px;
    width: 1122px;
    height: 654px;
    background:
      radial-gradient(circle at 40% 60%, var(--gold-light) 0%, var(--gold-mid) 18%, transparent 32%),
      radial-gradient(ellipse at 80% 25%, var(--gold-light) 0%, transparent 40%),
      radial-gradient(ellipse at 15% 30%, var(--gold-light) 0%, transparent 35%),
      linear-gradient(135deg, var(--gold-mid) 0%, var(--gold-deep) 40%, var(--gold-mid) 65%, var(--gold-deep) 100%);
  }
  .contact,
  .company,
  .region {
    position: absolute;
    margin: 0;
    font-family: "Lora", serif;
    font-style: italic;
    font-weight: 400;
    line-height: 1;
    color: var(--ink);
    white-space: nowrap;
  }
  .contact--phone,
  .contact--mobile { font-size: 45px; letter-spacing: 1px; left: 684px; }
  .contact--phone  { top: 50px; }
  .contact--mobile { top: 114px; }
  .contact--email,
  .contact--web    { font-size: 41px; left: 69px; }
  .contact--email  { top: 584px; }
  .contact--web    { top: 634px; }

  .company { left: 69px; top: 58px; font-size: 33px; }
  .region  { left: 69px; top: 102px; font-size: 24px; }

  .person-name,
  .person-title {
    position: absolute;
    margin: 0;
    font-family: "UnifrakturMaguntia", serif;
    font-weight: 400;
    color: var(--ink);
    white-space: nowrap;
    transform: translateX(-50%);
    line-height: 1;
  }
  .person-name  { left: 595px; top: 268px; font-size: 104px; }
  .person-title { left: 632px; top: 384px; font-size: 100px; }
</style>
</head>
<body>
  <main class="canvas">
    <div class="card-face" role="img" aria-label="Golden Indian-style ornamental pattern of swirls, paisley curves and a radiating sun, evoking India"></div>

    <svg class="guide-frame" width="1200" height="734" viewBox="0 0 1200 734" aria-hidden="true">
      <polyline points="39,41 1164,41 1164,698" fill="none" stroke="var(--bleed-blue)" stroke-width="4"/>
      <rect x="16" y="14" width="1172" height="707" fill="none" stroke="var(--trim-red)" stroke-width="3"/>
    </svg>

    <p class="company">Kestrel Trading Company</p>
    <p class="region">Papakura, Auckland, New Zealand</p>

    <p class="contact contact--phone">NZ Ph no.6493758162</p>
    <p class="contact contact--mobile">Mobile 6421603174</p>

    <h1 class="person-name">Briony Calder</h1>
    <h2 class="person-title">Director</h2>

    <p class="contact contact--email">Email briony@kestreltrading.co.nz</p>
    <p class="contact contact--web">Www.kestreltrading.co.nz</p>
  </main>
</body>
</html>
```